brivox new business card design project

we need a new business card design. you can view info about us @ brivox.com. i have attached an example of our previous card with our previous name that we no longer use. We really liked the design, colors etc. look below to see more info about this project. it asks for a limited number of words. please see our website for more info about our compnay.

Target Market(s)

law enforcement

Contact Information for Business Card

i have uploaded an example of what we used before that we liked.

Font styles to use
Serif

```html
<!DOCTYPE html>
<html lang="en">
<head>
<meta charset="utf-8">
<title>Brivox Business Card</title>
<link rel="stylesheet" href="https://fonts.googleapis.com/css2?family=Roboto:wght@300;400;700;900&display=swap">
<style>
  :root {
    --stage: #202122;
    --card: #0f2230;
    --card-deep: #0a1922;
    --ink: #ffffff;
    --accent: #3a86cf;
    --glow: #5cc4ff;
    --glow-soft: #1d5a86;
  }
  * { box-sizing: border-box; margin: 0; padding: 0; }
  html, body { width: 1200px; height: 1200px; overflow: hidden; }
  body {
    background: var(--stage);
    font-family: "Roboto", sans-serif;
    color: var(--ink);
    position: relative;
  }
  .card {
    position: absolute;
    left: 160px;
    width: 880px;
    height: 503px;
    background: linear-gradient(160deg, var(--card) 0%, var(--card-deep) 100%);
    overflow: hidden;
  }
  .card--front { top: 50px; }
  .card--back { top: 597px; }

  /* Front face */
  .network-map {
    position: absolute;
    left: 120px; top: 40px;
    width: 680px; height: 420px;
    border-radius: 44% 50% 46% 40% / 40% 38% 58% 52%;
    background:
      radial-gradient(ellipse at 45% 80%, rgba(92,196,255,0.55) 0%, rgba(29,90,134,0.35) 35%, rgba(29,90,134,0) 70%),
      radial-gradient(ellipse at 50% 50%, rgba(58,134,207,0.35) 0%, rgba(15,34,48,0) 75%);
  }
  .front-copy {
    position: absolute;
    left: 0; right: 0; top: 128px;
    text-align: center;
  }
  .wordmark {
    font-weight: 300;
    letter-spacing: 0.12em;
    color: var(--ink);
  }
  .front-copy .wordmark { font-size: 58px; line-height: 1; margin-bottom: 4px; }
  .headline {
    font-weight: 900;
    font-size: 50px;
    line-height: 1.02;
    letter-spacing: 0.02em;
  }
  .tagline {
    font-weight: 700;
    font-size: 17px;
    margin-top: 8px;
    letter-spacing: 0.02em;
  }

  /* Back face */
  .card--back .wordmark {
    position: absolute;
    right: 70px; top: 120px;
    font-size: 78px;
    line-height: 1;
  }
  .holder {
    position: absolute;
    left: 90px; top: 260px;
  }
  .holder-name { font-size: 30px; font-weight: 400; }
  .holder-title { font-size: 20px; color: var(--accent); margin-top: 2px; }
  .contact-list {
    list-style: none;
    margin-top: 22px;
  }
  .contact-list li {
    display: flex; align-items: center;
    font-size: 22px;
    line-height: 1.45;
  }
  .contact-list svg {
    width: 20px; height: 20px;
    margin-right: 14px;
    fill: none; stroke: var(--accent); stroke-width: 1.8;
  }
  .contact-list .icon-solid { fill: var(--accent); stroke: none; }
  .address {
    position: absolute;
    right: 70px; bottom: 70px;
    text-align: right;
    font-size: 22px;
    line-height: 1.4;
  }
</style>
</head>
<body>
  <section class="card card--front">
    <div class="network-map" role="img" aria-label="Glowing network illustration in the shape of a national map with connected points"></div>
    <div class="front-copy">
      <div class="wordmark">BRIVOX</div>
      <h1 class="headline">LAW ENFORCEMENT<br>INNOVATION</h1>
      <p class="tagline">Automating Processes and Connecting Jurisdictions</p>
    </div>
  </section>

  <section class="card card--back">
    <div class="wordmark">BRIVOX</div>
    <div class="holder">
      <p class="holder-name">Daniel Mercer</p>
      <p class="holder-title">CEO/Founder</p>
      <ul class="contact-list">
        <li>
          <svg viewBox="0 0 24 24"><path class="icon-solid" d="M6.6 10.8a15 15 0 0 0 6.6 6.6l2.2-2.2a1 1 0 0 1 1-.25 11.4 11.4 0 0 0 3.6.57 1 1 0 0 1 1 1V20a1 1 0 0 1-1 1A17 17 0 0 1 3 4a1 1 0 0 1 1-1h3.5a1 1 0 0 1 1 1c0 1.25.2 2.45.57 3.57a1 1 0 0 1-.25 1z"/></svg>
          866.555.0142
        </li>
        <li>
          <svg viewBox="0 0 24 24"><rect x="3" y="5" width="18" height="14"/><path d="M3 5l9 8 9-8"/></svg>
          info@brivox.com
        </li>
        <li>
          <svg viewBox="0 0 24 24"><circle cx="12" cy="12" r="9"/><ellipse cx="12" cy="12" rx="4" ry="9"/><path d="M3 12h18M5 7h14M5 17h14"/></svg>
          brivox.com
        </li>
      </ul>
    </div>
    <address class="address" style="font-style:normal">4120 Harmon Lane<br>Austin, TX 78701</address>
  </section>
</body>
</html>
```